Automotive component supplier needs a business card design

We need a business card design for our company called Velmar Global Components Ltd based in the UK. We are a supplier of interior and exterior components to premium car manufacturers such as Corvane Hale, Durrant Fyfe, Maxtorn and Valdessimo. We would like to see a modern business card design that uses the colour blue.

Target Market(s)

Premium automotive car manufacturers.

Industry/Entity Type

Automotive

Contact Information for Business Card

Company Name : Velmar Global Components Limited
Address: 17 Tamsey Yard, Upper Drisk, Warwick, CV31 8RJ, United Kingdom
Web Address : www.velmarparts-example.co.uk

Font styles to use
Other font styles liked:
• Helvetica

Colors
3176b5
0255a3
85acd3
cfdeed
cee9f5
85cae6
34a6d7
0692cd
9bcb3c

Requirements
Must have
• Clear company logo and a mixture of blue colours.
Nice to have
• A high quality modern image.
Should not have
• Multiple colours.

```html
<!DOCTYPE html>
<html lang="en">
<head>
<meta charset="utf-8">
<title>Velmar Global Components – Business Card</title>
<link href="https://fonts.googleapis.com/css2?family=Raleway:wght@400;700&family=Source+Sans+3:wght@400&display=swap" rel="stylesheet">
<style>
  :root {
    --brand-blue: #0b77bf;
    --deep-blue: #0255a3;
    --ink: #1e1e1e;
    --card: #ffffff;
    --backdrop: #eef1f4;
    --divider: #222222;
  }
  html, body {
    margin: 0;
    width: 1200px;
    height: 1200px;
    overflow: hidden;
    background: var(--backdrop);
  }
  .canvas {
    position: relative;
    width: 1200px;
    height: 1200px;
  }
  .card {
    position: absolute;
    background: var(--card);
    box-shadow: 0 10px 30px rgba(0,0,0,0.12);
  }
  .card--front { left: 288px; top: 150px; width: 624px; height: 388px; }
  .card--back  { left: 286px; top: 681px; width: 628px; height: 393px; }

  .brand {
    position: absolute;
    font-family: "Raleway", sans-serif;
    color: var(--brand-blue);
    line-height: 1;
  }
  .brand__name { display: block; font-weight: 700; }
  .brand__tagline { display: block; white-space: nowrap; font-weight: 700; }

  .card--front .brand { left: 34px; top: 164px; width: 248px; }
  .card--front .brand__name { font-size: 54px; letter-spacing: 3px; }
  .card--front .brand__tagline { font-size: 14px; letter-spacing: 4.2px; margin-top: 6px; }

  .divider {
    position: absolute;
    left: 304px; top: 106px;
    width: 2px; height: 178px;
    background: var(--divider);
  }
  .contacts {
    position: absolute;
    left: 320px; top: 118px;
    margin: 0; padding: 0;
    list-style: none;
    font-family: "Source Sans 3", sans-serif;
    font-size: 15px;
    color: var(--ink);
    line-height: 19px;
  }
  .contacts li {
    display: flex;
    align-items: flex-start;
    margin-bottom: 8px;
  }
  .contacts svg {
    width: 14px; height: 14px;
    margin: 2px 8px 0 0;
    flex: none;
    fill: var(--brand-blue);
  }

  .card--back .brand {
    left: 0; right: 0; top: 146px;
    text-align: center;
  }
  .card--back .brand__name { font-size: 86px; letter-spacing: 5px; }
  .card--back .brand__tagline { font-size: 20px; letter-spacing: 6px; margin-top: 10px; }

  .website {
    position: absolute;
    left: 0; right: 0; top: 316px;
    margin: 0;
    text-align: center;
    font-family: "Raleway", sans-serif;
    font-size: 14px;
    color: var(--deep-blue);
    letter-spacing: 0.3px;
  }
</style>
</head>
<body>
<main class="canvas">

  <section class="card card--front" aria-label="Business card front">
    <div class="brand">
      <span class="brand__name">VELMAR</span>
      <span class="brand__tagline">GLOBAL COMPONENTS</span>
    </div>
    <div class="divider"></div>
    <ul class="contacts">
      <li>
        <svg viewBox="0 0 14 14"><path d="M7 0a5 5 0 0 0-5 5c0 3.5 5 9 5 9s5-5.5 5-9a5 5 0 0 0-5-5zm0 7a2 2 0 1 1 0-4 2 2 0 0 1 0 4z"/></svg>
        <span>17 Tamsey Yard, Upper Drisk,<br>Warwick, CV31 8RJ, United Kingdom</span>
      </li>
      <li>
        <svg viewBox="0 0 14 14"><path d="M1 5c0-2 3-3 6-3s6 1 6 3v1h-3V5H4v1H1zM3 7h8l1 5H2zm4 1.5a1.5 1.5 0 1 0 0 3 1.5 1.5 0 0 0 0-3z"/></svg>
        <span>000 000 0000</span>
      </li>
      <li>
        <svg viewBox="0 0 14 14"><path d="M4 0h6a1 1 0 0 1 1 1v12a1 1 0 0 1-1 1H4a1 1 0 0 1-1-1V1a1 1 0 0 1 1-1zm.5 1.5v9h5v-9zM7 11.3a.8.8 0 1 0 0 1.6.8.8 0 0 0 0-1.6z"/></svg>
        <span>000 000 0000</span>
      </li>
      <li>
        <svg viewBox="0 0 14 14"><path d="M1 4h12v7H1zm1 1v.3l5 3 5-3V5z"/></svg>
        <span>info@velmarparts-example.co.uk</span>
      </li>
      <li>
        <svg viewBox="0 0 14 14"><g fill="none" stroke="#0b77bf" stroke-width="1"><circle cx="7" cy="7" r="6"/><ellipse cx="7" cy="7" rx="2.6" ry="6"/><path d="M1 7h12M2 4h10M2 10h10"/></g></svg>
        <span>www.velmarparts-example.co.uk</span>
      </li>
    </ul>
  </section>

  <section class="card card--back" aria-label="Business card back">
    <div class="brand">
      <span class="brand__name">VELMAR</span>
      <span class="brand__tagline">GLOBAL COMPONENTS</span>
    </div>
    <p class="website">WWW.VELMARPARTS-EXAMPLE.CO.UK</p>
  </section>

</main>
</body>
</html>
```